Koveli Seafood Shipping Packaging Re-Design

We need a packaging (Shipping Carton) design for our Seafood Products (FROZEN). We already have a basic packaging design which we prefer to have a modern touch on it.
Spec :
1. It must show our logo (Attached), note that the text of "KOVELI" which accompany the logo is optional, it can be omitted & showing only the logo.
2. Main color is Blue
3. Our carton is regular shipping box with dimension L43cm x W 27cm x H 16cm.
4. Our material of Carton is both Brown & White Kraft Paperboard, so the design should look nice in both material.

Attached our Logo and packaging design.

Target Market(s)

Frozen Seafood Distributor & Seafood Buyer

Industry/Entity Type

Food Production

Requirements
Must have
• 1. Must Show our Logo
• 2. Main Color of the Text/Logo is Blue
• 3. On the side of the packaging / Carton must show two box of CODE & SIZE
• 4. Must Show these icons :
• a. Handle with Care
• b. Maximum Stackable 10 Carton
• c. Recyleable Material
• d. Protect from the Water/Rain
Nice to have
• Would prefer to have a modern design

```html
<!DOCTYPE html>
<html lang="en">
<head>
<meta charset="utf-8">
<title>Koveli Seafood Shipping Carton – Dieline</title>
<link rel="stylesheet" href="https://fonts.googleapis.com/css2?family=Oswald:wght@500;700&display=swap">
<style>
  :root {
    --brand-blue: #1b6a98;
    --brand-blue-deep: #155a84;
    --label-blue: #a9d3f1;
    --paper: #f7f7f7;
    --paper-shade: #e9e9ea;
    --page: #ffffff;
  }
  * { box-sizing: border-box; margin: 0; padding: 0; }
  html, body { width: 1200px; height: 1200px; overflow: hidden; background: var(--page); }
  .canvas { position: relative; width: 1200px; height: 1200px; }
  .dieline { position: absolute; left: 20px; top: 478px; width: 1158px; height: 245px; }

  .flap { position: absolute; top: 0; height: 112px; width: 356px;
          background: linear-gradient(180deg, #f3f3f3 0%, #ebebeb 100%); }
  .flap--plain { left: 0; }
  .flap--branded { left: 578px; overflow: hidden; }
  .flap__band { position: absolute; left: 0; right: 0; bottom: 0; height: 36px; background: var(--brand-blue); }
  .flap__label { position: absolute; top: 86px; height: 14px; background: var(--label-blue); }
  .flap__label--a { left: 24px; width: 44px; }
  .flap__label--b { left: 73px; width: 45px; }
  .flap__badge { position: absolute; left: 252px; top: 8px; width: 90px; text-align: center;
                 color: var(--brand-blue); font: 700 11px/1.15 "Oswald", sans-serif; letter-spacing: .5px; }
  .flap__badge .dot { display: block; width: 22px; height: 22px; margin: 0 auto 4px;
                      border: 2px solid var(--brand-blue); border-radius: 50%; }

  .band { position: absolute; left: 0; top: 112px; width: 1158px; height: 28px; background: var(--brand-blue); }
  .icons { position: absolute; top: 117px; display: flex; gap: 5px; }
  .icons svg { width: 18px; height: 18px; }

  .panel { position: absolute; top: 140px; height: 105px; overflow: hidden;
           background: linear-gradient(180deg, var(--paper) 0%, #ffffff 45%, var(--paper-shade) 100%); }
  .panel--long { width: 356px; }
  .panel--short { width: 223px; }
  .panel__edge { position: absolute; left: 0; right: 0; bottom: 0; height: 10px;
                 background: linear-gradient(180deg, rgba(27,106,152,0) 0%, var(--brand-blue) 100%); }
  .panel__side { position: absolute; top: 0; bottom: 0; width: 4px; background: var(--brand-blue); }

  .temp { position: absolute; left: 48px; top: 43px; width: 56px; height: 20px;
          border: 1.5px solid var(--brand-blue); display: flex; align-items: center; gap: 3px; padding-left: 3px;
          color: var(--brand-blue); font: 500 15px/1 "Oswald", sans-serif; }
  .temp svg { width: 8px; height: 16px; }

  .mark { position: absolute; width: 84px; height: 84px; border-radius: 50%;
          background: radial-gradient(circle at 50% 45%, #ffffff 0%, #eef1f4 100%);
          border: 1px solid #e0e3e6; display: flex; align-items: center; justify-content: center;
          color: var(--brand-blue); font: 700 16px/1 "Oswald", sans-serif; letter-spacing: .5px; }
  .panel--long .mark { left: 136px; top: 10px; }
  .panel--short .mark { left: 120px; top: 10px; }

  .brand-word { position: absolute; left: 252px; top: 38px; color: var(--brand-blue);
                font: 700 22px/1 "Oswald", sans-serif; letter-spacing: 1px; }

  .spec { position: absolute; left: 26px; width: 64px; height: 21px; display: flex;
          border: 1px solid var(--brand-blue); }
  .spec--size { top: 26px; }
  .spec--code { top: 53px; }
  .spec__key { width: 24px; background: var(--brand-blue); color: #fff;
               font: 500 9px/19px "Oswald", sans-serif; text-align: center; }
</style>
</head>
<body>
<main class="canvas">
  <section class="dieline" aria-label="Shipping carton dieline">

    <div class="flap flap--plain"></div>
    <div class="flap flap--branded">
      <div class="flap__band" role="img" aria-label="Blue band with faint seafood doodle pattern"></div>
      <div class="flap__label flap__label--a"></div>
      <div class="flap__label flap__label--b"></div>
      <div class="flap__badge"><span class="dot"></span>KOVELI<br>SEAFOOD</div>
    </div>

    <div class="band" role="img" aria-label="Blue band with faint seafood doodle pattern"></div>

    <div class="icons" style="left:264px">
      <svg viewBox="0 0 20 20" aria-label="Handle with care"><circle cx="10" cy="10" r="9" fill="none" stroke="#fff" stroke-width="1.3"/><path d="M6 5h8l-1 5a3 3 0 0 1-6 0z M10 13v3 M7.5 16h5" fill="none" stroke="#fff" stroke-width="1.3"/></svg>
      <svg viewBox="0 0 20 20" aria-label="Protect from rain"><circle cx="10" cy="10" r="9" fill="none" stroke="#fff" stroke-width="1.3"/><path d="M4.5 10a5.5 5.5 0 0 1 11 0z M10 10v4.5a1.3 1.3 0 0 1-2.6 0" fill="none" stroke="#fff" stroke-width="1.3"/></svg>
      <svg viewBox="0 0 20 20" aria-label="Recyclable material"><circle cx="10" cy="10" r="9" fill="none" stroke="#fff" stroke-width="1.3"/><path d="M10 5l3 5H7z M6 14h8" fill="none" stroke="#fff" stroke-width="1.3"/></svg>
      <svg viewBox="0 0 20 20" aria-label="Maximum stack 10 cartons"><circle cx="10" cy="10" r="9" fill="none" stroke="#fff" stroke-width="1.3"/><rect x="6" y="5" width="8" height="3" fill="#fff"/><rect x="6" y="9" width="8" height="3" fill="#fff"/><rect x="6" y="13" width="8" height="3" fill="#fff"/></svg>
    </div>
    <div class="icons" style="left:842px">
      <svg viewBox="0 0 20 20" aria-label="Handle with care"><circle cx="10" cy="10" r="9" fill="none" stroke="#fff" stroke-width="1.3"/><path d="M6 5h8l-1 5a3 3 0 0 1-6 0z M10 13v3 M7.5 16h5" fill="none" stroke="#fff" stroke-width="1.3"/></svg>
      <svg viewBox="0 0 20 20" aria-label="Protect from rain"><circle cx="10" cy="10" r="9" fill="none" stroke="#fff" stroke-width="1.3"/><path d="M4.5 10a5.5 5.5 0 0 1 11 0z M10 10v4.5a1.3 1.3 0 0 1-2.6 0" fill="none" stroke="#fff" stroke-width="1.3"/></svg>
      <svg viewBox="0 0 20 20" aria-label="Recyclable material"><circle cx="10" cy="10" r="9" fill="none" stroke="#fff" stroke-width="1.3"/><path d="M10 5l3 5H7z M6 14h8" fill="none" stroke="#fff" stroke-width="1.3"/></svg>
      <svg viewBox="0 0 20 20" aria-label="Maximum stack 10 cartons"><circle cx="10" cy="10" r="9" fill="none" stroke="#fff" stroke-width="1.3"/><rect x="6" y="5" width="8" height="3" fill="#fff"/><rect x="6" y="9" width="8" height="3" fill="#fff"/><rect x="6" y="13" width="8" height="3" fill="#fff"/></svg>
    </div>

    <div class="panel panel--long" style="left:0">
      <div class="panel__edge" role="img" aria-label="Blue grunge border texture"></div>
      <div class="panel__side" style="left:0"></div>
      <div class="temp"><svg viewBox="0 0 8 16"><rect x="2.5" y="1" width="3" height="10" rx="1.5" fill="none" stroke="#1b6a98"/><circle cx="4" cy="13" r="2.5" fill="#1b6a98"/></svg>-18°C</div>
      <div class="mark">KOVELI</div>
      <div class="brand-word">KOVELI</div>
    </div>

    <div class="panel panel--short" style="left:356px">
      <div class="panel__edge" role="img" aria-label="Blue grunge border texture"></div>
      <div class="panel__side" style="left:0"></div>
      <div class="spec spec--size"><span class="spec__key">SIZE</span></div>
      <div class="spec spec--code"><span class="spec__key">CODE</span></div>
      <div class="mark">KOVELI</div>
    </div>

    <div class="panel panel--long" style="left:578px">
      <div class="panel__edge" role="img" aria-label="Blue grunge border texture"></div>
      <div class="panel__side" style="left:0"></div>
      <div class="temp"><svg viewBox="0 0 8 16"><rect x="2.5" y="1" width="3" height="10" rx="1.5" fill="none" stroke="#1b6a98"/><circle cx="4" cy="13" r="2.5" fill="#1b6a98"/></svg>-18°C</div>
      <div class="mark">KOVELI</div>
      <div class="brand-word">KOVELI</div>
    </div>

    <div class="panel panel--short" style="left:934px;width:224px">
      <div class="panel__edge" role="img" aria-label="Blue grunge border texture"></div>
      <div class="panel__side" style="left:0"></div>
      <div class="panel__side" style="right:0"></div>
      <div class="spec spec--size"><span class="spec__key">SIZE</span></div>
      <div class="spec spec--code"><span class="spec__key">CODE</span></div>
      <div class="mark">KOVELI</div>
    </div>

  </section>
</main>
</body>
</html>
```